Management consultant needs to update look of website

Currently I have a great word press website but it needs an updated look. I have new text for the site in the attached word document. I also have a list of websites whose design, look, and organization i like as a guide for the designer. The final design should be simple, strong, clear, and project the idea that my brand is a powerful authority in this space. Current site = www.brookfernadvisory.com

Target Market(s)

company owners / executives

Industry/Entity Type

Management Consulting

Number of Pages Required

3 page

Font styles to use
Serif

Colors

Designer to choose colors to be used in the design.

Requirements
Must have
• a simple and clear design and message. professional look. easy navigation. responsive to mobile devices. an easily implemented wordpress theme OR squarespace. use of my logo colors. though I am open to changing to a deep navy or charcoal logo image. source file uploaded.
Nice to have
• i like the cover photo and logo watermark on my current homepage. i like the google map with my logo on the current contact page. i like the animation as well. a great blend of the current site and something that is more seamless.

```html
<!DOCTYPE html>
<html lang="en">
<head>
<meta charset="utf-8">
<title>Brookfern Advisory</title>
<link href="https://fonts.googleapis.com/css2?family=Libre+Baskerville:wght@400;700&family=Lato:wght@400;700&display=swap" rel="stylesheet">
<style>
:root{
  --navy:#1f2a3c;
  --navy-deep:#161e2c;
  --gold:#c9a24a;
  --gold-soft:#d6b56c;
  --grey:#e4e4e4;
  --grey-mid:#cfcfcf;
  --white:#ffffff;
  --ink:#2b2b2b;
}
*{box-sizing:border-box;margin:0;padding:0}
html,body{width:1200px;height:3276px;overflow:hidden}
body{position:relative;background:var(--grey);font-family:"Lato",sans-serif;color:var(--ink)}
section,header,footer{position:absolute;left:0;width:1200px}

/* header + hero */
.hero{top:0;height:368px}
.hero-photo{position:absolute;inset:0;background:linear-gradient(160deg,#a9a397 0%,#6e6a62 45%,#3c3a36 100%)}
.topbar{position:absolute;top:0;left:0;width:1200px;height:56px;background:rgba(22,30,44,.85);display:flex;align-items:center;padding:0 40px}
.brand{display:flex;align-items:center;gap:10px;font-family:"Libre Baskerville",serif;color:var(--gold);font-size:17px;font-weight:700}
.brand-dot{width:30px;height:30px;border-radius:50%;border:2px solid var(--gold)}
.nav{margin-left:auto;display:flex;gap:34px;align-items:center}
.nav a{color:var(--white);font-size:13px;font-weight:700;letter-spacing:1px;text-decoration:none}
.nav a.cta{border:2px solid var(--gold);padding:8px 14px;border-radius:4px}
.banner{position:absolute;top:128px;left:290px;width:620px;height:62px;background:rgba(201,162,74,.92);color:var(--white);font-family:"Libre Baskerville",serif;font-size:24px;white-space:nowrap;display:flex;align-items:center;justify-content:center;gap:10px;letter-spacing:.5px}
.banner b{font-weight:400;font-size:30px}

/* intro */
.intro{top:400px;left:180px;width:840px;height:410px;background:var(--gold-soft);padding:40px 48px}
.intro h1{font-family:"Libre Baskerville",serif;font-size:22px;color:var(--navy);text-align:center;font-weight:400;white-space:nowrap;margin-bottom:30px}
.intro h1 b{color:var(--white);font-weight:400}
.intro p{color:var(--white);font-size:15px;line-height:1.75;margin-bottom:18px}

/* services */
.section-title{font-family:"Libre Baskerville",serif;color:var(--navy);font-size:26px;text-align:center;letter-spacing:1px}
.services{top:830px;height:480px}
.cards{position:absolute;top:52px;left:80px;display:flex;gap:40px}
.card{width:320px;height:420px;background:var(--navy);border-radius:6px;overflow:hidden;position:relative}
.card-photo{height:190px;background:linear-gradient(135deg,#b8b0a2,#6d675d)}
.card h3{font-family:"Libre Baskerville",serif;color:var(--gold);font-size:18px;text-align:center;margin:18px 0 10px;font-weight:400;white-space:nowrap}
.card p{color:var(--white);font-size:13.5px;line-height:1.6;padding:0 26px;text-align:center}
.more{position:absolute;right:24px;bottom:18px;color:var(--gold);font-size:13px;font-weight:700}

/* testimonials */
.testimonials{top:1340px;height:450px;background:var(--grey-mid)}
.t-head{text-align:center;margin-top:26px;font-family:"Libre Baskerville",serif;color:var(--navy);font-size:15px;line-height:1.5}
.t-head b{display:block;font-size:19px}
.t-row{position:absolute;top:100px;left:100px;display:flex;gap:30px}
.quote{width:320px;height:320px;background:var(--gold-soft);border-radius:6px;padding:26px}
.q-top{display:flex;align-items:center;gap:16px;margin-bottom:16px}
.avatar{width:78px;height:78px;border-radius:50%;background:linear-gradient(135deg,#ddd4c4,#8d8474);border:3px solid var(--white)}
.q-name{font-family:"Libre Baskerville",serif;color:var(--navy);font-size:16px}
.quote p{color:var(--white);font-size:13.5px;line-height:1.6}
.arrow{position:absolute;top:250px;width:34px;height:50px;background:#7a7a7a;display:flex;align-items:center;justify-content:center}

/* clients */
.clients{top:1810px;height:300px;background:var(--white)}
.clients .section-title{margin-top:26px}
.logo-grid{position:absolute;top:80px;left:130px;display:grid;grid-template-columns:repeat(7,100px);gap:26px 36px}
.partner{height:80px;display:flex;align-items:center;justify-content:center}
.partner span{display:block;background:#d9d9d9}
.sq{width:86px;height:44px;border-radius:6px}
.ci{width:66px;height:66px;border-radius:50%}

/* articles */
.articles{top:2110px;height:520px;background:var(--white)}
.articles .section-title{margin-top:14px}
.a-band{position:absolute;top:64px;left:0;width:1200px;height:270px;background:var(--navy)}
.a-row{position:absolute;top:92px;left:80px;display:flex;gap:40px}
.article{width:320px}
.a-photo{height:230px;position:relative;background:linear-gradient(135deg,#c4bcae,#6f695f)}
.date{position:absolute;top:0;left:22px;width:56px;height:64px;background:var(--gold);color:var(--white);font-size:11px;font-weight:700;text-align:center;padding-top:10px;line-height:1.4}
.article h4{font-family:"Libre Baskerville",serif;color:var(--gold);font-size:12px;margin:22px 0 8px;white-space:nowrap}
.article p{font-size:12.5px;line-height:1.6;color:#555}

/* contact */
.contact{top:2630px;height:570px}
.contact-bg{position:absolute;inset:0;background:linear-gradient(120deg,#b89a5c 0%,#8a7a5a 55%,#5d5850 100%)}
.addr{position:absolute;top:34px;left:70px;width:460px;height:500px;background:rgba(31,42,60,.9);padding:22px 30px}
.addr h5,.form h5{font-family:"Libre Baskerville",serif;color:var(--white);font-size:17px;text-align:center;font-weight:400;margin-bottom:16px}
.map{height:250px;background:linear-gradient(135deg,#e8e2cf,#c9d3c0)}
.addr p{color:var(--white);font-size:14px;line-height:1.6;margin-top:26px}
.phone{display:flex;align-items:center;gap:10px;color:var(--white);font-family:"Libre Baskerville",serif;font-size:17px;margin-top:22px;justify-content:center}
.form{position:absolute;top:34px;left:660px;width:460px}
.form h5 b{color:var(--gold);font-weight:400}
.field{height:40px;background:rgba(255,255,255,.9);margin-bottom:12px;padding:10px 14px;font-size:13px;color:#888}
.field.tall{height:170px}
.submit{margin:6px 0 0 auto;width:110px;height:40px;background:var(--navy);color:var(--white);font-weight:700;font-size:14px;display:flex;align-items:center;justify-content:center}

/* footer */
footer{top:3200px;height:76px;background:var(--navy-deep);display:flex;align-items:center;padding:0 40px;color:var(--white);font-size:13px}
footer .brand-dot{width:22px;height:22px;margin-right:10px}
footer nav{margin-left:auto;display:flex;gap:28px;color:var(--gold);font-weight:700}
</style>
</head>
<body>

<header class="hero">
  <div class="hero-photo" role="img" aria-label="Team of business people in a meeting around a table"></div>
  <div class="topbar">
    <div class="brand"><span class="brand-dot"></span>Brookfern Advisory</div>
    <nav class="nav">
      <a href="#">HOME</a><a href="#">ABOUT US</a><a href="#">SERVICES</a><a href="#">BLOG</a><a href="#" class="cta">CONTACT US</a>
    </nav>
  </div>
  <div class="banner">REQUEST A FREE <b>CONSULTATION</b></div>
</header>

<section class="intro">
  <h1>Great Companies <b>Succeed by</b> Investing <b>in the</b> Right People</h1>
  <p>It's no secret that long-term business success requires a smart investment in the right people for your company. And yet, knowing how to cultivate a strong staff and keep them focused on the road ahead can be challenging for even the savviest organizational leaders and human resource executives.</p>
  <p>Brookfern Advisory exists to help business owners, leaders, and HR teams understand how to identify, develop, and retain talented professionals who can take your company to the next level.</p>
</section>

<section class="services">
  <h2 class="section-title">SERVICES</h2>
  <div class="cards">
    <article class="card">
      <div class="card-photo" role="img" aria-label="Colleagues reviewing documents together"></div>
      <h3>TALENT STRATEGY</h3>
      <p>Business growth, even in the beginning, comes down to hiring the right talent and putting them in the right position to succeed.</p>
      <span class="more">Learn More</span>
    </article>
    <article class="card">
      <div class="card-photo" role="img" aria-label="Manager leading a workshop discussion"></div>
      <h3>MANAGEMENT WORKSHOPS</h3>
      <p>Bringing an expert in-house to get your leaders on the same page in terms of how to manage, how to lead, and how to raise up a workforce.</p>
      <span class="more">Learn More</span>
    </article>
    <article class="card">
      <div class="card-photo" role="img" aria-label="Executive in a one-on-one coaching session"></div>
      <h3>EXECUTIVE COACHING</h3>
      <p>I can be incredibly challenging to push yourself, or your company, to the next level without outside coaching and a fresh perspective.</p>
      <span class="more">Learn More</span>
    </article>
  </div>
</section>

<section class="testimonials">
  <div class="t-head">What Clients are Saying About<b>BROOKFERN ADVISORY</b></div>
  <div class="arrow" style="left:40px"><svg width="14" height="20"><path d="M12 2 L3 10 L12 18" fill="none" stroke="#fff" stroke-width="3"/></svg></div>
  <div class="arrow" style="right:40px"><svg width="14" height="20"><path d="M2 2 L11 10 L2 18" fill="none" stroke="#fff" stroke-width="3"/></svg></div>
  <div class="t-row">
    <div class="quote">
      <div class="q-top"><div class="avatar" role="img" aria-label="Client portrait"></div><span class="q-name">Daniel R.</span></div>
      <p>"Brookfern helped us rethink how we hire and develop our leaders. The team gave practical tools our managers use every day, and our retention has improved noticeably since the first workshop. I would recommend them to any owner."</p>
    </div>
    <div class="quote">
      <div class="q-top"><div class="avatar" role="img" aria-label="Client portrait"></div><span class="q-name">Marissa T.</span></div>
      <p>"Working with Brookfern changed how our executive team communicates. Their coaching was direct, honest and focused on results. We left each session with clear next steps and a stronger sense of where the company is headed."</p>
    </div>
    <div class="quote">
      <div class="q-top"><div class="avatar" role="img" aria-label="Client portrait"></div><span class="q-name">Owen K.</span></div>
      <p>"A thoughtful partner for any growing business. They took time to understand our culture before offering advice, and the talent strategy they built with us is still guiding our hiring decisions today."</p>
    </div>
  </div>
</section>

<section class="clients">
  <h2 class="section-title">CLIENTS &amp; PARTNERS</h2>
  <div class="logo-grid">
    <div class="partner"><span class="sq"></span></div>
    <div class="partner"><span class="ci"></span></div>
    <div class="partner"><span class="ci"></span></div>
    <div class="partner"><span class="sq"></span></div>
    <div class="partner"><span class="sq"></span></div>
    <div class="partner"><span class="sq"></span></div>
    <div class="partner"><span class="sq"></span></div>
    <div class="partner"><span class="ci"></span></div>
    <div class="partner"><span class="ci"></span></div>
    <div class="partner"><span class="sq"></span></div>
    <div class="partner"><span class="sq"></span></div>
    <div class="partner"><span class="ci"></span></div>
    <div class="partner"><span class="sq"></span></div>
  </div>
</section>

<section class="articles">
  <h2 class="section-title">LATEST ARTICLES</h2>
  <div class="a-band"></div>
  <div class="a-row">
    <article class="article">
      <div class="a-photo" role="img" aria-label="Team meeting in a bright office"><div class="date">12<br>MAR<br>2017</div></div>
      <h4>THE GROW-UP-OR-TUNE RULE</h4>
      <p>In your experience, is it better to promote from within or to hire outside talent? Here is how we think about building teams that last.</p>
    </article>
    <article class="article">
      <div class="a-photo" role="img" aria-label="Interview in progress sign on a door"><div class="date">04<br>MAR<br>2017</div></div>
      <h4>HOW TO ASK GREAT INTERVIEW QUESTIONS</h4>
      <p>If you are a manager, you are well aware that hiring the wrong person can become a liability. Asking the right questions is key.</p>
    </article>
    <article class="article">
      <div class="a-photo" role="img" aria-label="Frustrated professional at a laptop"><div class="date">21<br>FEB<br>2017</div></div>
      <h4>DEALING WITH FRUSTRATION AT WORK</h4>
      <p>Management can be stressful. Learning to handle frustration calmly sets the tone for everyone on your team and your results.</p>
    </article>
  </div>
</section>

<section class="contact">
  <div class="contact-bg" role="img" aria-label="Desk with laptop and notebook in warm light"></div>
  <div class="addr">
    <h5>ADDRESS</h5>
    <div class="map" role="img" aria-label="Regional map with office location marker"></div>
    <p>Brookfern Advisory is based in Riverton, and we serve clients nationwide.</p>
    <div class="phone">
      <svg width="18" height="18" viewBox="0 0 24 24"><path d="M6.6 10.8a15 15 0 0 0 6.6 6.6l2.2-2.2c.3-.3.7-.4 1-.2 1.1.4 2.3.6 3.6.6.6 0 1 .4 1 1V20c0 .6-.4 1-1 1A17 17 0 0 1 3 4c0-.6.4-1 1-1h3.5c.6 0 1 .4 1 1 0 1.3.2 2.5.6 3.6.1.3 0 .7-.2 1z" fill="#c9a24a"/></svg>
      PHONE: 555 - 014 - 2290
    </div>
  </div>
  <div class="form">
    <h5>REQUEST FOR A FREE <b>CONSULTATION</b></h5>
    <div class="field">Full Name</div>
    <div class="field">E-mail</div>
    <div class="field">Phone Number</div>
    <div class="field tall">Message</div>
    <div class="submit">Submit</div>
  </div>
</section>

<footer>
  <span class="brand-dot"></span>Brookfern Advisory Consulting © 2016
  <nav><span>Home</span><span>About</span><span>Contact</span></nav>
</footer>

</body>
</html>
```